Harbor Lantern Diagnostics
Stationary/Business Card
Project: Harbor Lantern Diagnostics
Harbor Lantern Diagnostics - Medical
Creative Brief
Use specific fonts
Font like in the uploaded pic (playing card)
Cutting-Edge
Marlo Quist
Chief Executive Officer
417 W Dunmore A Lubbock, Tx
marlo_047@quillpost.example
harborlanterndiagnostics.example
For the stationary I uploaded some ideas of how I would love for it to look like.
For the front and the back design of the business card, I have uploaded
orvell512 orvell512
I've already picked the winner for the logo but I'm still waiting on the finished product from the designer.

```html
<!DOCTYPE html>
<html lang="en">
<head>
<meta charset="utf-8">
<title>Harbor Lantern Diagnostics – Business Card</title>
<link rel="stylesheet" href="https://fonts.googleapis.com/css2?family=Cinzel:wght@400;600&family=Lato:wght@400;700&display=swap">
<style>
  :root {
    --stage: #2b2b2d;
    --card-white: #ffffff;
    --gold: #d9a824;
    --gold-light: #ecc85a;
    --maroon: #7a1518;
    --ink: #3a3a3a;
    --ink-on-gold: #3b2a06;
  }
  * { box-sizing: border-box; margin: 0; padding: 0; }
  html, body { width: 1200px; height: 746px; overflow: hidden; }
  body {
    background: var(--stage);
    display: flex;
    align-items: center;
    justify-content: center;
    gap: 60px;
    font-family: "Lato", Arial, sans-serif;
  }
  .card {
    position: relative;
    width: 520px;
    height: 297px;
    border-radius: 16px;
    background: var(--card-white);
    overflow: hidden;
  }
  .brand {
    position: absolute;
    display: flex;
    flex-direction: column;
    align-items: center;
    gap: 10px;
  }
  .brand-name {
    font-family: "Cinzel", Georgia, serif;
    font-weight: 400;
    color: var(--ink);
    letter-spacing: 1px;
    white-space: nowrap;
  }
  .brand-dot {
    border-radius: 50%;
    background: var(--maroon);
  }
  .card-front .brand { left: 0; right: 0; top: 92px; }
  .card-front .brand-name { font-size: 14px; }
  .card-front .brand-dot { width: 70px; height: 70px; }

  .card-back .wave { position: absolute; inset: 0; }
  .card-back .brand { left: 24px; top: 82px; }
  .card-back .brand-name { font-size: 12px; }
  .card-back .brand-dot { width: 62px; height: 62px; }

  .contact {
    position: absolute;
    right: 34px;
    top: 36px;
    color: var(--ink-on-gold);
    font-size: 10px;
  }
  .contact-name {
    font-family: "Cinzel", Georgia, serif;
    font-weight: 600;
    font-size: 13px;
    letter-spacing: 0.5px;
  }
  .contact-title { font-size: 9px; margin-bottom: 14px; }
  .contact-list { list-style: none; display: flex; flex-direction: column; gap: 6px; }
  .contact-list li { display: flex; align-items: center; gap: 8px; justify-content: flex-end; }
  .contact-list svg { width: 10px; height: 10px; fill: var(--maroon); }
  .address {
    position: absolute;
    right: 34px;
    bottom: 22px;
    font-size: 10px;
    color: var(--ink-on-gold);
    letter-spacing: 0.3px;
  }
</style>
</head>
<body>
  <section class="card card-front">
    <div class="brand">
      <span class="brand-name">Harbor Lantern Diagnostics</span>
      <span class="brand-dot"></span>
    </div>
  </section>

  <section class="card card-back">
    <svg class="wave" viewBox="0 0 520 297" preserveAspectRatio="none">
      <path fill="var(--maroon)" d="M318 0 C238 62 320 202 194 232 C118 250 40 240 0 250 L0 297 L520 297 L520 0 Z"/>
      <path fill="var(--gold)" d="M334 0 C254 62 336 214 206 244 C128 262 44 254 0 262 L0 297 L520 297 L520 0 Z"/>
    </svg>

    <div class="brand">
      <span class="brand-name">Harbor Lantern Diagnostics</span>
      <span class="brand-dot"></span>
    </div>

    <div class="contact">
      <p class="contact-name">Marlo Quist</p>
      <p class="contact-title">Chief Executive Officer</p>
      <ul class="contact-list">
        <li>806.555.0142
          <svg viewBox="0 0 10 10"><path d="M2 0h2l1 3-1.5 1a6 6 0 0 0 2.5 2.5L7 5l3 1v2a2 2 0 0 1-2 2A8 8 0 0 1 0 2a2 2 0 0 1 2-2z"/></svg></li>
        <li>806.555.0178
          <svg viewBox="0 0 10 10"><path d="M2 0h2l1 3-1.5 1a6 6 0 0 0 2.5 2.5L7 5l3 1v2a2 2 0 0 1-2 2A8 8 0 0 1 0 2a2 2 0 0 1 2-2z"/></svg></li>
        <li>806.555.0193
          <svg viewBox="0 0 10 10"><path d="M2 0h2l1 3-1.5 1a6 6 0 0 0 2.5 2.5L7 5l3 1v2a2 2 0 0 1-2 2A8 8 0 0 1 0 2a2 2 0 0 1 2-2z"/></svg></li>
        <li>marlo_047@quillpost.example
          <svg viewBox="0 0 10 10"><path d="M0 2h10v6H0z M0 2l5 3.5L10 2" fill="none" stroke="var(--maroon)" stroke-width="1"/></svg></li>
        <li>harborlanterndiagnostics.example
          <svg viewBox="0 0 10 10"><circle cx="5" cy="5" r="4.5"/></svg></li>
      </ul>
    </div>

    <p class="address">417 W Dunmore A Lubbock, Tx</p>
  </section>
</body>
</html>
```